Home Equity Lines of Credit
are BACK!!!

* Up to 97.5% on Owner Occupied Properties
* 700 Minimum Scores
* Fund in only 2-3 weeks

Can be used for...
* Education Expense
* Bill Consolidation
* Home Improvement
* Investments

Call today for more information!
(800) 647-2915

Bluecrest Lending Partners, Inc.
NMLS #318660
www.bluecrestlendhub.com

```html
<!DOCTYPE html>
<html lang="en">
<head>
<meta charset="utf-8">
<title>Home Equity Lines of Credit Are Back</title>
<link href="https://fonts.googleapis.com/css2?family=Oswald:wght@600;700&family=Montserrat:wght@500;600;700&display=swap" rel="stylesheet">
<style>
  :root {
    --brand-blue: #0862a9;
    --brand-olive: #aa9f21;
    --ink: #222222;
    --paper: #ffffff;
    --photo-warm: #b9a48c;
    --photo-cool: #7f8c97;
    --photo-green: #7d8b63;
  }
  * { margin: 0; padding: 0; box-sizing: border-box; }
  html, body { width: 1200px; height: 1200px; overflow: hidden; background: var(--paper); }
  .flyer { position: relative; width: 1200px; height: 1200px; background: var(--paper); font-family: "Montserrat", sans-serif; }
  .flyer__shapes { position: absolute; inset: 0; }
  .headline { position: absolute; left: 70px; color: var(--paper); font-family: "Oswald", sans-serif; font-weight: 700; text-transform: uppercase; white-space: nowrap; }
  .headline--top { top: 44px; font-size: 74px; line-height: 84px; letter-spacing: 0.5px; }
  .headline--back { top: 222px; font-size: 104px; line-height: 124px; letter-spacing: -1px; }
  .check-list { position: absolute; list-style: none; }
  .check-list li { position: relative; padding-left: 44px; font-weight: 600; white-space: nowrap; }
  .check-list li svg { position: absolute; left: 0; }
  .features { left: 70px; top: 370px; color: var(--ink); font-size: 27px; }
  .features li { line-height: 34px; margin-bottom: 9px; }
  .features li svg { top: 3px; width: 30px; height: 30px; }
  .features .features__wrap { display: block; }
  .uses-title { position: absolute; left: 712px; top: 620px; color: var(--paper); font-family: "Oswald", sans-serif; font-weight: 600; font-size: 46px; line-height: 56px; white-space: nowrap; }
  .uses { left: 712px; top: 690px; color: var(--paper); font-size: 31px; }
  .uses li { line-height: 40px; }
  .uses li svg { top: 5px; width: 30px; height: 30px; }
  .call-line { position: absolute; left: 68px; top: 868px; color: var(--paper); font-weight: 600; font-size: 34px; white-space: nowrap; }
  .phone-pill { position: absolute; left: 71px; top: 921px; width: 588px; height: 72px; background: var(--paper); border-radius: 36px; }
  .phone-pill__icon { position: absolute; left: -1px; top: -2px; width: 76px; height: 76px; }
  .phone-pill__number { position: absolute; left: 95px; top: 2px; color: var(--brand-blue); font-weight: 700; font-size: 56px; line-height: 68px; white-space: nowrap; }
  .company { position: absolute; left: 89px; top: 1040px; color: var(--ink); font-size: 25px; line-height: 46px; white-space: nowrap; }
  .company__name { color: var(--brand-blue); font-weight: 700; font-size: 26px; }
  .company__web { color: var(--ink); font-weight: 500; }
  .company__web b { color: var(--brand-blue); font-weight: 600; }
  .brand-mark { position: absolute; left: 706px; top: 1006px; display: flex; align-items: center; gap: 12px; }
  .brand-mark__dot { width: 22px; height: 22px; border-radius: 50%; background: var(--brand-olive); }
  .brand-mark__name { color: var(--brand-blue); font-weight: 700; font-size: 22px; white-space: nowrap; }
</style>
</head>
<body>
<main class="flyer">
  <svg class="flyer__shapes" width="1200" height="1200" viewBox="0 0 1200 1200">
    <defs>
      <linearGradient id="couple-tones" x1="0" y1="0" x2="1" y2="1">
        <stop offset="0" stop-color="#d9d4cc"/>
        <stop offset="0.5" stop-color="var(--photo-warm)"/>
        <stop offset="1" stop-color="#334b6e"/>
      </linearGradient>
      <linearGradient id="graduate-tones" x1="0" y1="0" x2="1" y2="1">
        <stop offset="0" stop-color="#c9bba3"/>
        <stop offset="0.55" stop-color="var(--photo-green)"/>
        <stop offset="1" stop-color="#1f2533"/>
      </linearGradient>
    </defs>
    <polygon role="img" aria-label="Photo: a worried couple reviewing bills with a laptop on a living room sofa" points="520,0 1200,0 1200,589 635,589 520,346" fill="url(#couple-tones)"/>
    <polygon role="img" aria-label="Photo: a smiling graduate in cap and gown holding a diploma outside a campus building" points="0,552 530,552 650,847 0,847" fill="url(#graduate-tones)"/>
    <polygon class="band-blue" points="0,0 520,0 631,227 0,227" fill="var(--brand-blue)"/>
    <polygon class="band-olive" points="0,227 631,227 689,346 0,346" fill="var(--brand-olive)"/>
    <polygon class="call-band" points="0,847 650,847 731,868 658,1017 0,1017" fill="var(--brand-olive)"/>
    <polygon class="uses-panel" points="548,589 1200,589 1200,868 684,868" fill="var(--brand-blue)"/>
    <polygon class="uses-tag" points="641,616 1080,616 1118,682 680,682" fill="var(--brand-olive)"/>
    <polygon class="footer-strip" points="644,1189 1200,1189 1200,1200 639,1200" fill="var(--brand-blue)"/>
  </svg>

  <h1 class="headline headline--top">Home Equity<br>Lines of Credit</h1>
  <div class="headline headline--back">Are Back!!!</div>

  <ul class="check-list features">
    <li><svg viewBox="0 0 30 30"><circle cx="15" cy="15" r="12.5" fill="none" stroke="var(--brand-blue)" stroke-width="2.2"/><path d="M9.5 15.5l4 4 7-8" fill="none" stroke="var(--brand-blue)" stroke-width="2.2"/></svg>Up to 97.5% on<span class="features__wrap">Owner Occupied Properties</span></li>
    <li><svg viewBox="0 0 30 30"><circle cx="15" cy="15" r="12.5" fill="none" stroke="var(--brand-blue)" stroke-width="2.2"/><path d="M9.5 15.5l4 4 7-8" fill="none" stroke="var(--brand-blue)" stroke-width="2.2"/></svg>700 Minimum Scores</li>
    <li><svg viewBox="0 0 30 30"><circle cx="15" cy="15" r="12.5" fill="none" stroke="var(--brand-blue)" stroke-width="2.2"/><path d="M9.5 15.5l4 4 7-8" fill="none" stroke="var(--brand-blue)" stroke-width="2.2"/></svg>Fund in only 2-3 weeks</li>
  </ul>

  <h2 class="uses-title">CAN BE USED FOR...</h2>
  <ul class="check-list uses">
    <li><svg viewBox="0 0 30 30"><circle cx="15" cy="15" r="12.5" fill="none" stroke="#fff" stroke-width="2.2"/><path d="M9.5 15.5l4 4 7-8" fill="none" stroke="#fff" stroke-width="2.2"/></svg>Education Expense</li>
    <li><svg viewBox="0 0 30 30"><circle cx="15" cy="15" r="12.5" fill="none" stroke="#fff" stroke-width="2.2"/><path d="M9.5 15.5l4 4 7-8" fill="none" stroke="#fff" stroke-width="2.2"/></svg>Bill Consolidation</li>
    <li><svg viewBox="0 0 30 30"><circle cx="15" cy="15" r="12.5" fill="none" stroke="#fff" stroke-width="2.2"/><path d="M9.5 15.5l4 4 7-8" fill="none" stroke="#fff" stroke-width="2.2"/></svg>Home Improvement</li>
    <li><svg viewBox="0 0 30 30"><circle cx="15" cy="15" r="12.5" fill="none" stroke="#fff" stroke-width="2.2"/><path d="M9.5 15.5l4 4 7-8" fill="none" stroke="#fff" stroke-width="2.2"/></svg>Investments</li>
  </ul>

  <p class="call-line">Call today for more information!</p>
  <div class="phone-pill">
    <svg class="phone-pill__icon" viewBox="0 0 76 76">
      <circle cx="38" cy="38" r="36" fill="var(--brand-blue)" stroke="#fff" stroke-width="4"/>
      <path d="M27 20c2-1 4 0 5 2l3 7c1 2 0 3-1 4l-3 2c2 5 6 10 11 13l2-3c1-1 3-2 4-1l7 3c2 1 3 3 2 5l-2 4c-2 3-6 3-10 1-10-5-17-13-21-23-1-4 0-8 3-10z" fill="#fff"/>
    </svg>
    <span class="phone-pill__number">(800) 647-2915</span>
  </div>

  <div class="company">
    <div class="company__name">Bluecrest Lending Partners, Inc.</div>
    <div class="company__nmls">NMLS #318660</div>
    <div class="company__web">www.<b>bluecrestlendhub</b>.com</div>
  </div>

  <div class="brand-mark">
    <span class="brand-mark__dot"></span>
    <span class="brand-mark__name">Bluecrest Lending Partners, Inc.</span>
  </div>
</main>
</body>
</html>
```